VORLEN Website Design

We need a website designed for our company VORLEN. We are a luxury lifestyle club that will provide benefits and services for our members. The site should be clean & sleek, preferably using black and white (or darker colors). (example sites: brimvale.example, tusko.example)

Here is a link of a sample page I did using wix. (https://pelmundry4.sitebuild.example/mypage) This can be used to get a general idea.

Target Market(s)

Upper Middle Class in the United States

Number of Pages Required

5+ page

Font styles to use
Sans Serif
Other font styles liked:
• Arial (or other similar fonts)

Requirements
Must have
• A clean design that is eye-catching and speaks to our company.
Nice to have
• Ideas for copy.

```html
<!DOCTYPE html>
<html lang="en">
<head>
<meta charset="utf-8">
<title>VORLEN – A Members Only Lifestyle Club</title>
<link href="https://fonts.googleapis.com/css2?family=Arimo:ital,wght@0,400;0,700;1,400&display=swap" rel="stylesheet">
<style>
:root{
  --ink:#111111;
  --text:#222222;
  --muted:#444444;
  --white:#ffffff;
  --paper:#efefef;
  --footer:#2b2b2b;
  --line:#333333;
  --soft-line:#8a8a8a;
}
*{box-sizing:border-box;margin:0;padding:0}
html,body{width:1200px;height:3974px;overflow:hidden}
body{font-family:"Arimo",Arial,sans-serif;color:var(--text);background:var(--white);position:relative}
.abs{position:absolute}
.center{left:0;width:1200px;text-align:center}
.band{position:absolute;left:0;width:1200px}

/* hero */
.hero{top:0;height:715px;background:radial-gradient(ellipse at 30% 35%,#6a3a2e 0%,#3a1c18 40%,#1a0e0c 75%),#1a0e0c;overflow:hidden}
.hero-shade{position:absolute;inset:0;background:linear-gradient(180deg,rgba(0,0,0,.35),rgba(0,0,0,.15) 50%,rgba(0,0,0,.45))}
.lang{left:118px;top:10px;color:var(--white);font-size:13px;display:flex;align-items:center;gap:6px}
.login{right:118px;top:10px;color:var(--white);font-size:13px;display:flex;align-items:center;gap:6px}
.brand{font-weight:700;color:var(--white);font-size:38px;letter-spacing:1px}
.hero .brand{top:18px}
.nav{top:74px;display:flex;justify-content:center;gap:26px;color:var(--white);font-size:12px}
.hero-title{top:288px;color:var(--white);font-size:37px;font-weight:700;letter-spacing:.5px}
.hero-sub{top:333px;color:var(--white);font-size:13px}
.btn{position:absolute;height:45px;border-radius:23px;font-size:12px;display:flex;align-items:center;justify-content:center;text-transform:uppercase;letter-spacing:.3px}
.btn-ghost-light{border:2px solid var(--white);color:var(--white)}
.btn-solid-light{background:var(--white);color:var(--ink)}
.btn-outline{border:1.5px solid var(--ink);color:var(--ink);background:transparent}
.hero-arrows{top:496px;left:520px;width:160px;height:30px}

/* section headings */
.section-title{font-size:24px;font-weight:400;color:var(--ink);letter-spacing:.5px}
.rule{position:absolute;left:560px;width:80px;height:2px;background:var(--soft-line)}

/* services */
.services{top:715px;height:1113px;background:var(--paper)}
.sub-title{font-size:19px;font-weight:700;color:var(--ink)}
.intro{font-size:13px;font-style:italic;color:var(--muted);line-height:27px}
.service-photo{position:absolute;width:233px;height:233px;border-radius:50%;border:7px solid var(--white);box-shadow:0 4px 10px rgba(0,0,0,.25)}
.service-name{position:absolute;width:320px;text-align:center;font-size:18px;font-weight:700;color:var(--ink)}

/* about */
.about{top:1828px;height:398px;background:var(--white)}
.about-text{font-size:13px;line-height:24px;color:var(--text)}

/* newsletter */
.news{top:2226px;height:829px;background:var(--paper)}
.card{position:absolute;top:158px;width:316px;height:517px;background:var(--white)}
.card-photo{position:absolute;left:0;top:0;width:316px;height:283px}
.tag{position:absolute;left:12px;top:20px;background:var(--white);font-size:12px;font-style:italic;padding:5px 12px}
.card-title{position:absolute;left:22px;top:312px;width:280px;font-size:13px;font-weight:700;line-height:18px;color:var(--ink)}
.card-meta{position:absolute;left:22px;top:362px;font-size:12px;font-style:italic;display:flex;gap:40px;color:var(--text)}
.card-meta span{display:flex;align-items:center;gap:7px}
.card-text{position:absolute;left:22px;top:390px;width:272px;font-size:13px;font-style:italic;color:var(--muted);line-height:21px;text-align:justify}
.card-foot{position:absolute;left:22px;right:22px;top:480px;display:flex;justify-content:space-between;align-items:center;font-size:12px;font-style:italic}
.dots{letter-spacing:3px;font-size:14px;font-style:normal}
.share{display:flex;align-items:center;gap:5px;text-decoration:underline}

/* subscribe */
.subscribe{top:3055px;height:248px;background:var(--white)}
.subscribe-lead{font-size:23px;line-height:33px;color:var(--ink)}
.email-field{position:absolute;left:371px;top:167px;width:331px;height:45px;border:1.5px solid var(--ink);border-radius:23px;font-size:12px;font-style:italic;padding:15px 22px}
.submit{position:absolute;left:710px;top:167px;width:122px;height:45px;border-radius:23px;background:var(--ink);color:var(--white);font-size:12px;display:flex;align-items:center;justify-content:center}

/* contact */
.contact{top:3303px;height:401px;background:var(--paper)}
.field{position:absolute;border-bottom:1.5px solid var(--line);font-size:12px;font-style:italic;padding-bottom:8px;color:var(--muted)}

/* footer */
.site-footer{top:3704px;height:270px;background:var(--footer)}
.site-footer .brand{top:26px}
.site-footer .nav{top:90px}
.socials{top:138px;display:flex;justify-content:center;gap:24px}
.socials span{width:18px;height:18px;border-radius:50%;background:var(--white)}
.footer-rule{position:absolute;left:120px;top:196px;width:960px;height:1px;background:#6a6a6a}
.copyright{top:223px;color:var(--white);font-size:12px}
</style>
</head>
<body>

<section class="band hero" role="img" aria-label="Friends raising glasses of red wine in a warm, dim lounge">
  <div class="hero-shade"></div>
  <div class="abs lang">
    <svg width="13" height="13" viewBox="0 0 13 13"><circle cx="6.5" cy="6.5" r="5.5" fill="none" stroke="#fff" stroke-width="1.3"/><path d="M1 6.5h11M6.5 1c-2.5 3-2.5 8 0 11M6.5 1c2.5 3 2.5 8 0 11" fill="none" stroke="#fff" stroke-width="1"/></svg>EN
  </div>
  <div class="abs login">
    <svg width="13" height="13" viewBox="0 0 13 13"><path d="M2 11 11 2M5 2h6v6" fill="none" stroke="#fff" stroke-width="1.6"/></svg>Login
  </div>
  <div class="abs center brand">VORLEN</div>
  <nav class="abs center nav"><span>Home</span><span>About</span><span>Services &amp; Benifits</span><span>Noted</span><span>Contact</span></nav>
  <h1 class="abs center hero-title">A MEMBERS ONLY LIFESTYLE CLUB</h1>
  <p class="abs center hero-sub">Lorem Ipsum is simply dummy text of the printing and typesetting industry.</p>
  <div class="btn btn-ghost-light" style="left:425px;top:375px;width:167px">Learn More</div>
  <div class="btn btn-solid-light" style="left:609px;top:375px;width:200px">Apply for Membership</div>
  <svg class="abs hero-arrows" viewBox="0 0 160 30"><path d="M13 8 4 15l9 7z" fill="none" stroke="#fff" stroke-width="2"/><line x1="80" y1="2" x2="80" y2="28" stroke="#fff" stroke-width="1" opacity=".6"/><path d="M140 8l9 7-9 7z" fill="#fff"/></svg>
</section>

<section class="band services">
  <h2 class="abs center section-title" style="top:88px">SERVICES &amp; BENIFTS</h2>
  <div class="rule" style="top:137px"></div>
  <h3 class="abs center sub-title" style="top:173px">WE ARE VORLEN</h3>
  <p class="abs center intro" style="top:202px">Built in the image of a "Multi-Family Office", VORLEN provides members with access to just about any service, experience, and event desirable.<br>VORLEN is truly the most exclusive lifestyle club out there.</p>

  <div class="service-photo" role="img" aria-label="Hands working a calculator over financial papers" style="left:173px;top:300px;background:radial-gradient(circle at 40% 40%,#f2f2f2,#9aa3ad 70%,#4b535b)"></div>
  <div class="service-name" style="left:129px;top:568px">ACCOUNTING SERVICES</div>
  <div class="service-photo" role="img" aria-label="Bar chart on paper beside a small potted tree and coins" style="left:485px;top:300px;background:linear-gradient(160deg,#f5f5f5 30%,#4d7ab0 55%,#5b7a3e 80%)"></div>
  <div class="service-name" style="left:441px;top:568px">INVESTMENT SERVICES</div>
  <div class="service-photo" role="img" aria-label="Lawyer at a desk with scales of justice and a gavel" style="left:795px;top:300px;background:radial-gradient(circle at 60% 40%,#e8e4dc,#8a7356 60%,#2c2620)"></div>
  <div class="service-name" style="left:751px;top:568px">LAWYER SERVICES</div>

  <div class="service-photo" role="img" aria-label="Row of modern townhouses" style="left:173px;top:638px;background:linear-gradient(180deg,#cfe0ee 30%,#e6e1d8 50%,#8b7b69 80%)"></div>
  <div class="service-name" style="left:129px;top:906px">REAL ESTATE SERVICES</div>
  <div class="service-photo" role="img" aria-label="Concierge desk with a service bell" style="left:485px;top:638px;background:radial-gradient(circle at 45% 60%,#c9c9c9,#6e6e6e 55%,#e9e9e9)"></div>
  <div class="service-name" style="left:441px;top:906px">24/7 CONCIERGE</div>
  <div class="service-photo" role="img" aria-label="Private jet flying above the clouds" style="left:795px;top:638px;background:linear-gradient(180deg,#bfd3e6,#f4f6f8 60%,#dfe6ec)"></div>
  <div class="service-name" style="left:751px;top:906px">PRIVATE JET TRAVEL</div>

  <div class="btn btn-outline" style="left:518px;top:1019px;width:165px">View All Services</div>
</section>

<section class="band about">
  <h2 class="abs center section-title" style="top:60px">ABOUT US</h2>
  <div class="rule" style="top:109px"></div>
  <p class="abs center about-text" style="top:141px">Lorem Ipsum is simply dummy text of the printing and typesetting industry. Lorem Ipsum has been the industry's standard dummy<br>text ever since the 1500s, when an unknown printer took a galley of type and scrambled it to make a type specimen book. It has<br>survived not only five centuries, but also the leap into electronic typesetting, remaining essentially unchanged.</p>
  <p class="abs center about-text" style="top:220px">It was popularised in the 1960s with the release of Typeline sheets containing Lorem Ipsum passages, and more recently with<br>desktop publishing software like Quillset Layout including versions of Lorem Ipsum.</p>
  <div class="btn btn-outline" style="left:518px;top:300px;width:165px">Read More</div>
</section>

<section class="band news">
  <h2 class="abs center section-title" style="top:66px">NEWSLETTER</h2>
  <div class="rule" style="top:115px"></div>

  <article class="card" style="left:122px">
    <div class="card-photo" role="img" aria-label="Couple with luggage looking out an airport window at a plane" style="background:linear-gradient(180deg,#d8e6f2,#a9c3d8 55%,#5a5550)"></div>
    <div class="tag">Lifestyle, Travel</div>
    <h4 class="card-title">How Ashcombe Club's revamp has Elevated The Golfing lifestyle</h4>
    <div class="card-meta"><span>&#9638; 10/10/2018</span><span>&#9679; Comments (2)</span></div>
    <p class="card-text">Lorem Ipsum is simply dummy text of the printing and typesetting industry. Lorem Ipsum has been the industry's standard dummy text ever since the 1500s.</p>
    <div class="card-foot"><span class="dots">&#9679;&#9679;&#9679;</span><span class="share"><svg width="12" height="10" viewBox="0 0 12 10"><path d="M1 9c1-4 4-5 7-5V1l4 4-4 4V6C5 6 3 7 1 9z" fill="#111"/></svg>Share</span></div>
  </article>

  <article class="card" style="left:442px">
    <div class="card-photo" role="img" aria-label="Aerial view of a sandy beach curving between turquoise sea and green hills" style="background:linear-gradient(135deg,#2d8aa6 0%,#4fb3c2 45%,#e6d3a6 55%,#7b8a4e 80%)"></div>
    <div class="tag">Travel</div>
    <h4 class="card-title">A Heavenly Experience On Turkey</h4>
    <div class="card-meta"><span>&#9638; 10/10/2018</span><span>&#9679; Comments (2)</span></div>
    <p class="card-text">Lorem Ipsum is simply dummy text of the printing and typesetting industry. Lorem Ipsum has been the industry's standard dummy text ever since the 1500s.</p>
    <div class="card-foot"><span class="dots">&#9679;&#9679;&#9679;</span><span class="share"><svg width="12" height="10" viewBox="0 0 12 10"><path d="M1 9c1-4 4-5 7-5V1l4 4-4 4V6C5 6 3 7 1 9z" fill="#111"/></svg>Share</span></div>
  </article>

  <article class="card" style="left:766px">
    <div class="card-photo" role="img" aria-label="Banquet hall decorated with purple lighting and candle centrepieces" style="background:radial-gradient(ellipse at 50% 70%,#e07ad0,#7a1e86 45%,#240a33)"></div>
    <div class="tag">Events</div>
    <h4 class="card-title">Decoration For Private Events</h4>
    <div class="card-meta"><span>&#9638; 10/10/2018</span><span>&#9679; Comments (2)</span></div>
    <p class="card-text">Lorem Ipsum is simply dummy text of the printing and typesetting industry. Lorem Ipsum has been the industry's standard dummy text ever since the 1500s.</p>
    <div class="card-foot"><span class="dots">&#9679;&#9679;&#9679;</span><span class="share"><svg width="12" height="10" viewBox="0 0 12 10"><path d="M1 9c1-4 4-5 7-5V1l4 4-4 4V6C5 6 3 7 1 9z" fill="#111"/></svg>Share</span></div>
  </article>

  <div class="btn btn-outline" style="left:518px;top:729px;width:165px">Read More</div>
</section>

<section class="band subscribe">
  <p class="abs center subscribe-lead" style="top:58px">Subscribe to the latest news and experiences in<br>global luxury, contemporary culture, and exclusive offers</p>
  <div class="email-field">Email Address</div>
  <div class="submit">SUBMIT</div>
</section>

<section class="band contact">
  <h2 class="abs center section-title" style="top:48px">CONTACT US</h2>
  <div class="rule" style="top:97px"></div>
  <div class="field" style="left:270px;top:148px;width:207px">Name</div>
  <div class="field" style="left:495px;top:148px;width:207px">Email Address</div>
  <div class="field" style="left:723px;top:148px;width:207px">Phone Number</div>
  <div class="field" style="left:270px;top:220px;width:660px">Message</div>
  <div class="btn btn-outline" style="left:518px;top:306px;width:165px">Send</div>
</section>

<footer class="band site-footer">
  <div class="abs center brand">VORLEN</div>
  <nav class="abs center nav"><span>Home</span><span>About</span><span>Services &amp; Benifits</span><span>Noted</span><span>Contact</span></nav>
  <div class="abs center socials"><span></span><span></span><span></span><span></span><span></span></div>
  <div class="footer-rule"></div>
  <p class="abs center copyright">© Copyright 2018 Vorlen. All Right Reserved</p>
</footer>

</body>
</html>
```